Website for new crypto research organization

See brief (attached). This is a pretty basic website with only a handful of pages + ability to collect email addresses.

```html
<!DOCTYPE html>
<html lang="en">
<head>
<meta charset="utf-8">
<title>Tidewell Digital</title>
<link href="https://fonts.googleapis.com/css2?family=Roboto:wght@300;400;500;700;900&display=swap" rel="stylesheet">
<style>
:root{
  --teal:#04a7a1;
  --navy:#151a33;
  --ink:#161a2a;
  --card-dark:#151824;
  --page:#f7f8f9;
  --white:#ffffff;
  --muted:#6f7380;
  --line:#d9dde2;
  --stage:#eef9f9;
  --art-dark:#2b2a30;
  --art-warm:#c9a24a;
}
*{margin:0;padding:0;box-sizing:border-box}
html,body{width:1200px;height:2599px;overflow:hidden;background:var(--stage);font-family:'Roboto',sans-serif;color:var(--ink)}
.page{position:relative;width:1200px;height:2567px;background:var(--page);overflow:hidden}
.abs{position:absolute}

/* header */
.site-header{left:0;top:0;width:1200px;height:60px;background:var(--white)}
.brand{left:149px;top:16px;display:flex;align-items:center;gap:7px;font-weight:700;font-size:13px;color:var(--teal)}
.brand-mark{width:12px;height:12px;border:2px solid var(--teal)}
.main-nav{left:0;top:0;height:60px;width:1200px}
.main-nav a{position:absolute;top:21px;font-size:13px;font-weight:500;color:var(--ink);text-decoration:none}
.main-nav a.active{color:var(--teal)}

/* hero */
.hero-title{left:149px;top:270px;font-size:66px;font-weight:700;letter-spacing:5px;color:var(--teal)}
.hero-text{left:149px;top:374px;width:410px;font-size:12.5px;line-height:21px;font-weight:300;color:var(--muted)}
.art-fill{background:linear-gradient(135deg,var(--art-dark),#4a4236 60%,var(--art-warm))}
.hero-art{left:604px;top:184px;width:485px;height:379px}

/* about */
.section-title{font-weight:700;color:var(--navy)}
.about-title{left:0;width:1200px;top:660px;text-align:center;font-size:40px}
.about-text{left:300px;width:600px;top:734px;text-align:center;font-size:12.5px;line-height:21px;color:#555a66}

/* process */
.process-title{left:149px;top:876px;font-size:29px;font-weight:700;color:var(--navy)}
.process-arrow{left:458px;top:900px}
.timeline{left:149px;top:1043px;width:901px;height:1px;background:var(--line)}
.timeline-dot{left:146px;top:1040px;width:7px;height:7px;border-radius:50%;border:1.5px solid var(--teal);background:var(--white)}
.step-badge{width:38px;height:38px;border-radius:50%;background:var(--navy);color:var(--white);font-size:13px;font-weight:700;display:flex;align-items:center;justify-content:center;top:977px}
.step-badge.first{background:var(--teal)}
.step-stem{width:1px;background:#9fb4bd;top:1015px}
.step-text{width:148px;text-align:center;font-size:11.5px;line-height:17.5px;color:#555a66}

/* reports */
.reports-title{left:149px;top:1330px;font-size:41px;color:var(--navy)}
.reports-rule{left:149px;top:1382px;width:71px;height:4px;background:var(--teal)}
.art-reports{left:1058px;top:1277px;width:142px;height:160px}
.report-card{top:1437px;width:400px;height:400px;background:var(--white);border-right:1px solid #e6e8eb;border-bottom:1px solid #e6e8eb;padding:41px 41px 0}
.report-card.featured{background:var(--card-dark);border-color:var(--card-dark)}
.report-date{font-size:12px;color:var(--teal)}
.report-name{margin-top:16px;font-size:27px;line-height:35px;font-weight:700;color:var(--navy)}
.featured .report-name{color:var(--white)}
.report-link{position:absolute;left:41px;top:342px;font-size:12.5px;color:var(--teal);text-decoration:none}

/* subscribe */
.subscribe-title{left:0;width:1200px;top:1945px;text-align:center;font-size:44px;line-height:57px}
.email-field{left:384px;top:2099px;width:281px;height:55px;border:1.5px solid #9aa0aa;background:var(--white);padding-left:17px;font-size:13px;line-height:52px;color:#8a8f99}
.subscribe-btn{left:674px;top:2099px;width:141px;height:55px;background:var(--teal);color:var(--white);font-size:13px;font-weight:700;display:flex;align-items:center;justify-content:center}
.art-left{left:0;top:2091px;width:153px;height:171px}
.art-right{left:996px;top:2141px;width:204px;height:121px}

/* footer */
.site-footer{left:0;top:2262px;width:1200px;height:305px;background:var(--white);border-top:2px solid var(--teal)}
.footer-brand{left:149px;top:2312px;display:flex;align-items:center;gap:9px;font-size:22px;font-weight:700;color:var(--teal)}
.footer-brand .brand-mark{width:18px;height:18px}
.disclaimer{left:149px;top:2392px;width:430px;font-size:9.5px;line-height:15.5px;color:#3d4150}
.footer-heading{top:2313px;font-size:15px;font-weight:500;color:var(--navy)}
.footer-rule{top:2337px;width:17px;height:2px;background:var(--teal)}
.footer-links{left:730px;top:2359px;list-style:none}
.footer-links li{font-size:13.5px;line-height:28.4px;color:var(--ink)}
.social{top:2356px;width:26px;height:26px;border-radius:50%;background:var(--navy)}
</style>
</head>
<body>
<div class="page">

  <header class="site-header abs">
    <div class="brand abs"><span class="brand-mark"></span>TIDEWELL</div>
    <nav class="main-nav abs">
      <a class="active" href="#" style="left:651px">Home</a>
      <a href="#" style="left:717px">About</a>
      <a href="#" style="left:784px">Research</a>
      <a href="#" style="left:870px">News</a>
      <a href="#" style="left:932px">Careers</a>
      <a href="#" style="left:1010px">Media</a>
    </nav>
  </header>

  <section class="hero">
    <h1 class="hero-title abs">TIDEWELL</h1>
    <p class="hero-text abs">Northgate Ledger Capital is a founder-led cryptoasset investment firm comprised of team members who've honed their skills as technology entrepreneurs, operators, venture capitalists, researchers, and</p>
    <div class="hero-art art-fill abs" role="img" aria-label="Graffiti illustration of a large gold coin surrounded by spray cans and splashes"></div>
  </section>

  <section class="about">
    <h2 class="section-title about-title abs">About us</h2>
    <p class="about-text abs">Northgate Ledger Capital is a founder-led cryptoasset investment firm comprised of team members who've honed their skills as technology entrepreneurs, operators, venture capitalists, researchers, and advisors.</p>
  </section>

  <section class="process">
    <h3 class="process-title abs">Our research process</h3>
    <svg class="process-arrow abs" width="44" height="56" viewBox="0 0 44 56" fill="none" stroke="#04a7a1" stroke-width="1.6" stroke-linecap="round">
      <path d="M3 4 C24 2 42 18 22 50"/>
      <path d="M17 43 L22 50 L29 46"/>
    </svg>
    <div class="timeline abs"></div>
    <div class="timeline-dot abs"></div>

    <div class="step-badge first abs" style="left:309px">01</div>
    <div class="step-stem abs" style="left:328px;height:63px"></div>
    <p class="step-text abs" style="left:254px;top:1083px">Stone Age development of Agriculture on the fluvial plains</p>

    <div class="step-badge abs" style="left:507px">02</div>
    <div class="step-stem abs" style="left:526px;height:113px"></div>
    <p class="step-text abs" style="left:452px;top:1135px">Stone Age development of Agriculture on the fluvial plains</p>

    <div class="step-badge abs" style="left:706px">03</div>
    <div class="step-stem abs" style="left:725px;height:63px"></div>
    <p class="step-text abs" style="left:651px;top:1083px">Stone Age development of Agriculture on the fluvial plains</p>

    <div class="step-badge abs" style="left:905px">04</div>
    <div class="step-stem abs" style="left:924px;height:113px"></div>
    <p class="step-text abs" style="left:850px;top:1135px">Stone Age development of Agriculture on the fluvial plains</p>
  </section>

  <section class="reports">
    <h2 class="section-title reports-title abs">Recent research reports</h2>
    <div class="reports-rule abs"></div>
    <div class="art-fill art-reports abs" role="img" aria-label="Graffiti illustration of spray cans and a skateboard"></div>

    <article class="report-card featured abs" style="left:0">
      <p class="report-date">28.1.2022</p>
      <h3 class="report-name">Oracle Network Valuations: The VSPT Ratio</h3>
      <a class="report-link" href="#">LEARN MORE</a>
    </article>
    <article class="report-card abs" style="left:400px">
      <p class="report-date">28.1.2022</p>
      <h3 class="report-name">Relay Mesh<br>Investment Thesis</h3>
      <a class="report-link" href="#">LEARN MORE</a>
    </article>
    <article class="report-card abs" style="left:800px">
      <p class="report-date">28.1.2022</p>
      <h3 class="report-name">The Regulatory State -<br>22 Predictions for 2022</h3>
      <a class="report-link" href="#">LEARN MORE</a>
    </article>
  </section>

  <section class="subscribe">
    <h2 class="section-title subscribe-title abs">Subscribe to Tidewell<br>Digital Insights</h2>
    <div class="email-field abs">Type your email</div>
    <div class="subscribe-btn abs">SUBSCRIBE</div>
    <div class="art-fill art-left abs" role="img" aria-label="Graffiti illustration of winged spray cans"></div>
    <div class="art-fill art-right abs" role="img" aria-label="Graffiti illustration of spray cans and splashes"></div>
  </section>

  <footer class="site-footer abs"></footer>
  <div class="footer-brand abs"><span class="brand-mark"></span>TIDEWELL</div>
  <p class="disclaimer abs">This site is not intended to provide any investment, financial, legal, regulatory, accounting, tax or similar advice, and nothing on this site should be construed as a recommendation by Brightfield IM, LLC, its affiliates, or any third party, to acquire or dispose of any investment, or to engage in any investment strategy or transaction. An investment in any strategy involves a high degree of risk and there is always the possibility of loss, including the loss of principal. Nothing in this site may be considered as an offer or solicitation to purchase or sell securities or other services. For more information please see our terms of use.</p>

  <h4 class="footer-heading abs" style="left:730px">Navigation</h4>
  <div class="footer-rule abs" style="left:730px"></div>
  <ul class="footer-links abs">
    <li>Home</li><li>About</li><li>Research</li><li>News</li><li>Careers</li><li>Media</li>
  </ul>

  <h4 class="footer-heading abs" style="left:912px">Follow us</h4>
  <div class="footer-rule abs" style="left:912px"></div>
  <div class="social abs" style="left:912px" aria-label="Social profile"></div>
  <div class="social abs" style="left:947px" aria-label="Social profile"></div>

</div>
</body>
</html>
```